We need a postcard design to promote the book written by our founder and president, Rick Tolver. The book is titled KESTRAL: The Craft and Method of Persuasion. We're open to any eye-catching image designs you come up with.

```html
<!DOCTYPE html>
<html lang="en">
<head>
<meta charset="utf-8">
<title>KESTRAL Book Postcard</title>
<link rel="stylesheet" href="https://fonts.googleapis.com/css2?family=Montserrat:wght@300;400;700;800&family=Open+Sans:wght@400;600;700&display=swap">
<style>
  :root {
    --page: #ecebe8;
    --card: #ffffff;
    --ink: #2b2b2e;
    --purple: #5b3f8c;
    --night: #1d1f29;
    --night-violet: #2c2540;
    --rule: #9a9a9e;
    --stamp: #d6d6d8;
    --line: #b9b9bd;
  }
  * { box-sizing: border-box; margin: 0; padding: 0; }
  html, body { width: 1200px; height: 1200px; overflow: hidden; background: var(--page); }
  body { position: relative; font-family: "Open Sans", sans-serif; color: var(--ink); }

  .postcard {
    position: absolute; left: 180px; width: 840px; height: 560px;
    background: var(--card); overflow: hidden;
    box-shadow: 0 2px 10px rgba(0,0,0,.12);
  }
  .postcard--front { top: 28px; }
  .postcard--back { top: 612px; }

  /* FRONT */
  .headline { position: absolute; left: 40px; top: 30px; font-family: "Montserrat", sans-serif; line-height: 1.02; }
  .headline span { display: block; }
  .headline__strong { color: var(--purple); font-weight: 800; font-size: 38px; letter-spacing: .5px; }
  .headline__light { color: var(--ink); font-weight: 400; font-size: 32px; letter-spacing: 1px; }
  .headline__strong--small { font-size: 34px; }

  .hero {
    position: absolute; left: 330px; top: 30px; width: 470px; height: 250px;
    background: linear-gradient(180deg, #15141f 0%, #2e2546 38%, #5a4258 62%, #a8683d 84%, #1a1512 100%);
  }
  .hero__frame {
    position: absolute; left: 70px; top: 78px; width: 330px; height: 92px;
    border: 2px solid rgba(255,255,255,.75);
    display: flex; align-items: center; justify-content: center; text-align: center;
    font-family: "Montserrat", sans-serif; font-weight: 300; color: #f2f2f2;
    font-size: 27px; line-height: 1.08; letter-spacing: 1px;
  }
  .accent-rule { position: absolute; background: var(--rule); }
  .accent-rule--top { left: 600px; top: 16px; width: 215px; height: 4px; }
  .accent-rule--right { left: 813px; top: 16px; width: 4px; height: 120px; }
  .accent-rule--left { left: 318px; top: 150px; width: 4px; height: 142px; }
  .accent-rule--bottom { left: 318px; top: 290px; width: 200px; height: 4px; }

  .intro { position: absolute; left: 40px; top: 154px; width: 268px; font-size: 12px; line-height: 1.35; text-align: justify; }
  .story { position: absolute; left: 40px; top: 302px; width: 770px; font-size: 12px; line-height: 1.35; }
  .story p + p { margin-top: 6px; }
  .story strong { font-weight: 700; }
  .signoff { position: absolute; right: 32px; top: 424px; font-size: 12px; font-weight: 600; line-height: 1.35; text-align: left; }
  .invite { position: absolute; left: 40px; top: 426px; width: 480px; color: var(--purple); font-weight: 700; font-size: 13px; line-height: 1.35; }

  .callband { position: absolute; left: 0; top: 0; width: 840px; height: 560px; }
  .callband__text {
    position: absolute; left: 40px; top: 506px; display: flex; align-items: center; gap: 14px;
    color: #fff; font-size: 20px; font-weight: 600;
  }
  .callband__number { font-size: 22px; letter-spacing: .5px; }

  /* BACK */
  .section { position: absolute; left: 0; width: 440px; padding: 0 28px 0 40px; font-size: 12.4px; line-height: 1.4; text-align: justify; }
  .section__title { font-family: "Open Sans", sans-serif; font-weight: 700; font-size: 14px; color: var(--purple); margin-bottom: 2px; text-align: left; }
  .section--who { top: 40px; height: 160px; }
  .section--what { top: 200px; height: 178px; padding-top: 16px; color: #f1f1f4; background: linear-gradient(100deg, var(--night) 0%, var(--night-violet) 70%, #3e3160 100%); }
  .section--what .section__title { color: #ffffff; }
  .section--why { top: 392px; }
  .divider { position: absolute; left: 452px; top: 30px; width: 4px; height: 500px; background: var(--rule); }
  .stamp { position: absolute; right: 44px; top: 36px; width: 76px; height: 76px; background: var(--stamp); }
  .address-line { position: absolute; left: 500px; width: 296px; height: 1px; background: var(--line); }
</style>
</head>
<body>

<article class="postcard postcard--front" aria-label="Postcard front">
  <div class="accent-rule accent-rule--top"></div>
  <div class="accent-rule accent-rule--right"></div>
  <div class="accent-rule accent-rule--left"></div>
  <div class="accent-rule accent-rule--bottom"></div>

  <h1 class="headline">
    <span class="headline__strong">LEADERSHIP</span>
    <span class="headline__light">IS THE ABILITY</span>
    <span class="headline__strong headline__strong--small">TO INFLUENCE</span>
  </h1>

  <div class="hero" role="img" aria-label="Photo of a lone figure standing on a hill under a starry night sky, glowing orange on the horizon">
    <div class="hero__frame">A NEW GENERATION<br>OF CHANGE</div>
  </div>

  <p class="intro">If you want to enact change in your business, you can't do it alone; you have to recruit and rally all of your employees behind the cause. But your employees are adults, so they're probably a little stubborn and set in their ways, which means getting them to change can be quite the feat indeed.</p>

  <div class="story">
    <p>Over the years, we've worked with thousands of businesses, and we came to realize just how important the skill of adult behavior change actually is and how challenging it is to implement it well. Those experiences led us to refine the KESTRAL methodology for influencing adult behavior, which in turn led to the book you now hold in your hands, <strong>KESTRAL: The Craft and Method of Persuasion.</strong></p>
    <p>We thought you'd appreciate KESTRAL, and maybe even glean some fresh insights for your own leadership role.<br>KESTRAL is also the methodology at the core of all our products here at The Halvern Group, so if you like the book,<br>be sure to give our website a gander, too (that's at HalvernGroup.net).</p>
  </div>

  <p class="signoff">Happy Reading!<br>Rick Tolver/The Halvern Group Team</p>

  <svg class="callband" viewBox="0 0 840 560" aria-hidden="true">
    <polygon points="0,484 520,484 538,462 612,462 628,474 840,474 840,560 0,560" fill="#1d1f29"/>
  </svg>

  <p class="invite">We'd love to chat about the perils, pitfalls, and positives of<br>leadership with you, from one leader to another.</p>

  <div class="callband__text">
    <span>Give us a call at</span>
    <svg width="22" height="22" viewBox="0 0 24 24" aria-hidden="true">
      <circle cx="12" cy="12" r="10.5" fill="none" stroke="#fff" stroke-width="1.6"/>
      <path d="M8.6 7.2c.4-.4 1-.4 1.3 0l1 1.3c.3.4.3.9 0 1.2l-.6.6c.5 1.2 1.4 2.1 2.6 2.6l.6-.6c.3-.3.8-.3 1.2 0l1.3 1c.4.3.4.9 0 1.3l-.8.8c-.6.6-1.6.7-2.4.3-2.2-1.1-3.900-2.8-5-5-.4-.8-.3-1.8.3-2.4z" fill="#fff"/>
    </svg>
    <span class="callband__number">1-800-555-0142.</span>
  </div>
</article>

<article class="postcard postcard--back" aria-label="Postcard back">
  <section class="section section--who">
    <h2 class="section__title">WHO WE ARE</h2>
    <p>We are The Halvern Group, a charmingly incongruous and blatantly genuine group of big thinkers and list makers. Get us together, and our ideas bloom into vibrant, sky-high projects; take us apart, and we work methodically and assiduously to accomplish the goals we created together. We say there's no mountain too high or ambition too big, for us or our clients.</p>
  </section>

  <section class="section section--what">
    <h2 class="section__title">WHAT WE DO</h2>
    <p>We create and implement practical courses and curriculum to help businesses &amp; individuals grow. With a varied team of experienced coaches and analyzers, we help diagnose and alleviate obstacles in both business-to-business and business-to-consumer enterprises across dozens of industries in order to increase profits &amp; actualize a comprehensive vision for their business.</p>
  </section>

  <section class="section section--why">
    <h2 class="section__title">WHY WE DO IT</h2>
    <p>We believe that, when outfitted with the right tools, every business can succeed. We believe that the most decisive factor in that success is effective leadership. And we believe that we're the organization that can help every business, regardless of size or industry, change, learn and grow through strong leadership, a clear vision, and a little elbow grease.</p>
  </section>

  <div class="divider"></div>
  <div class="stamp" aria-label="Stamp area"></div>
  <div class="address-line" style="top:200px"></div>
  <div class="address-line" style="top:250px"></div>
  <div class="address-line" style="top:300px"></div>
</article>

</body>
</html>
```